Business Card Design Project

Hi,
This is a simple contest. The logo for the back of the card is deigned. See attached files. The front of the card must have :

Directors Name: Dorian
Mob:
e-mail:
Postal Address:
Web Page Adress:

It may also add words: "Leaders in Construction Project Management Services"

Target Market(s)

Business & Home owners alike

Industry/Entity Type

Business

Requirements
Must have
• See details above and logo attached
Should not have
• Images other than logo

```html
<!DOCTYPE html>
<html lang="en">
<head>
<meta charset="utf-8">
<title>Keystone Projects – Business Card</title>
<link rel="stylesheet" href="https://fonts.googleapis.com/css2?family=Oswald:wght@500;700&display=swap">
<style>
  :root {
    --bg: #ececec;
    --brand-blue: #009ddd;
    --ink-white: #ffffff;
    --ink-black: #000000;
    --stripe-black: #0a0a0a;
    --card-white: #ffffff;
  }
  * { margin: 0; padding: 0; box-sizing: border-box; }
  html, body {
    width: 1200px; height: 1000px; overflow: hidden;
    background: var(--bg);
    font-family: "Oswald", "Arial Narrow", sans-serif;
  }
  .card {
    position: absolute;
    left: 338px;
    width: 525px;
    height: 303px;
    background: var(--brand-blue);
    overflow: hidden;
  }
  .card--front { top: 157px; }
  .card--back  { top: 541px; }

  .wordmark {
    position: absolute;
    display: flex;
    align-items: center;
    gap: 10px;
    color: var(--ink-white);
    font-weight: 700;
    letter-spacing: 0.5px;
    white-space: nowrap;
  }
  .wordmark__square {
    width: 40px; height: 40px;
    background: var(--ink-white);
  }
  .wordmark__name { font-size: 30px; line-height: 1; }
  .card--front .wordmark { left: 140px; top: 129px; }
  .card--back .wordmark { left: 20px; top: 97px; }

  .tagline {
    position: absolute;
    right: 20px; top: 44px;
    text-align: right;
    color: var(--ink-white);
    font-weight: 500;
    font-size: 10.5px;
    line-height: 14px;
  }
  .person {
    position: absolute;
    right: 19px; top: 96px;
    text-align: right;
  }
  .person__name {
    color: var(--ink-white);
    font-weight: 700;
    font-size: 16px;
    line-height: 22px;
  }
  .person__role {
    color: var(--ink-black);
    font-weight: 500;
    font-size: 11px;
    line-height: 14px;
  }
  .contact {
    position: absolute;
    right: 19px; top: 151px;
    list-style: none;
  }
  .contact__item {
    display: flex;
    justify-content: flex-end;
    align-items: center;
    gap: 5px;
    height: 17px;
    color: var(--ink-white);
    font-weight: 500;
    font-size: 7.5px;
  }
  .contact__icon { width: 14px; height: 14px; }

  .card__base {
    position: absolute;
    left: 0; top: 227px;
    width: 100%; height: 76px;
    background: var(--card-white);
  }
  .card__stripe {
    position: absolute;
    left: 0; top: 230px;
    width: 100%; height: 6px;
    background: var(--stripe-black);
  }
</style>
</head>
<body>

<section class="card card--front">
  <div class="wordmark">
    <span class="wordmark__square"></span>
    <span class="wordmark__name">KEYSTONE PROJECTS</span>
  </div>
</section>

<section class="card card--back">
  <div class="wordmark">
    <span class="wordmark__square"></span>
    <span class="wordmark__name">KEYSTONE PROJECTS</span>
  </div>

  <p class="tagline">“Leaders in Construction<br>Project Management Services”</p>

  <div class="person">
    <p class="person__name">DORIAN</p>
    <p class="person__role">Director</p>
  </div>

  <ul class="contact">
    <li class="contact__item">(02) 5550 4821
      <svg class="contact__icon" viewBox="0 0 14 14" fill="none" stroke="#000" stroke-width="1.2">
        <circle cx="7" cy="7" r="6"/>
        <path d="M4.5 4c.3 2.6 2.3 4.8 5 5.5l.8-1.2-1.4-.8-.6.7c-1-.5-1.7-1.2-2.2-2.2l.7-.6-.8-1.4z" fill="#000" stroke="none"/>
      </svg>
    </li>
    <li class="contact__item">dorian@keystonemail.com
      <svg class="contact__icon" viewBox="0 0 14 14" fill="none" stroke="#000" stroke-width="1.2">
        <rect x="1" y="3" width="12" height="8"/>
        <path d="M1 3l6 4.5L13 3M1 11l4.5-4M13 11l-4.5-4"/>
      </svg>
    </li>
    <li class="contact__item">27 Harbour St Riverton NSW 2199
      <svg class="contact__icon" viewBox="0 0 14 14" fill="#000">
        <path d="M7 1L0.5 7h2v6h3.5V9.5h2V13H11.5V7h2z"/>
      </svg>
    </li>
    <li class="contact__item">www.keystoneprojects.com
      <svg class="contact__icon" viewBox="0 0 14 14" fill="none" stroke="#000" stroke-width="1">
        <circle cx="7" cy="7" r="6"/>
        <ellipse cx="7" cy="7" rx="2.6" ry="6"/>
        <path d="M1 7h12M2 4h10M2 10h10"/>
      </svg>
    </li>
  </ul>

  <div class="card__base"></div>
  <div class="card__stripe"></div>
</section>

</body>
</html>
```